High-end residential home builder needs a business card design

We need a new business card design for a small residential construction company based in Boise, Idaho. We specialize in building custom high-end homes and remodels, with a focus on great design and craftsmanship.

We would like to use our current logo, but open to new color suggestions.
Just looking for a clean, sharp, modern design that looks high-end.

Target Market(s)

Upscale clientele

Industry/Entity Type

Contractor

Contact Information for Business Card

Company: Stonefield Custom Builders
Name: Marcus Tilley
Phone number: 208 367 4120
Email: MarcusTilleySCB@mailbox-example.com
Website: Stonefieldcustombuilders-example.com

Font styles to use
Serif
Sans Serif

Requirements
Must have
• Company Logo
Company name
My name
My phone number
My email
Company website
Nice to have
• I have attached a few photos of cards that I really like.

```html
<!DOCTYPE html>
<html lang="en">
<head>
<meta charset="utf-8">
<title>Stonefield Custom Builders – Business Card</title>
<link rel="stylesheet" href="https://fonts.googleapis.com/css2?family=Montserrat:wght@400;600;700&display=swap">
<style>
  :root {
    --bg-light: #e6e6e6;
    --bg-dark: #bdbdbd;
    --card: #232323;
    --card-deep: #1b1b1b;
    --orange: #e8891c;
    --text-light: #d9d9d9;
    --white: #ffffff;
    --silver: #9a9a9a;
  }
  * { box-sizing: border-box; margin: 0; padding: 0; }
  html, body { width: 1200px; height: 800px; overflow: hidden; }
  body {
    background: radial-gradient(ellipse at 40% 30%, var(--bg-light), var(--bg-dark));
    font-family: "Montserrat", sans-serif;
    position: relative;
  }
  .card {
    position: absolute;
    width: 540px;
    height: 308px;
    background: linear-gradient(135deg, var(--card), var(--card-deep));
    border-bottom: 3px solid var(--orange);
    box-shadow: 0 14px 30px rgba(0,0,0,0.35);
    overflow: hidden;
  }
  .card--contact { left: 70px; top: 100px; }
  .card--brand { left: 590px; top: 392px; }

  /* Contact side */
  .contact {
    position: absolute;
    left: 36px;
    bottom: 46px;
    width: 250px;
  }
  .contact__name {
    color: var(--orange);
    font-weight: 700;
    font-size: 23px;
    letter-spacing: 0.5px;
    text-transform: uppercase;
    white-space: nowrap;
  }
  .contact__rule {
    width: 52px;
    height: 1px;
    background: var(--orange);
    margin: 12px 0 14px;
  }
  .contact__list { list-style: none; }
  .contact__item {
    display: flex;
    align-items: center;
    gap: 8px;
    color: var(--text-light);
    font-size: 11px;
    line-height: 20px;
    white-space: nowrap;
  }
  .contact__icon { width: 10px; height: 10px; flex: none; }

  /* Large tone-on-tone name mark */
  .mark-large {
    position: absolute;
    top: 54px;
    display: flex;
    align-items: center;
    justify-content: center;
    width: 200px;
    height: 200px;
    border: 2px solid var(--silver);
  }
  .mark-large__name {
    color: var(--silver);
    font-weight: 600;
    font-size: 21px;
    text-transform: uppercase;
    letter-spacing: 2px;
  }
  .card--contact .mark-large { right: 30px; }
  .card--brand .mark-large { left: 30px; }

  /* Brand lockup */
  .brand {
    position: absolute;
    right: 30px;
    top: 133px;
    display: flex;
    align-items: center;
    gap: 14px;
  }
  .brand__square {
    width: 42px;
    height: 42px;
    border: 2px solid var(--orange);
  }
  .brand__name {
    color: var(--white);
    font-weight: 600;
    font-size: 13px;
    letter-spacing: 3px;
    text-transform: uppercase;
    line-height: 1.5;
  }
</style>
</head>
<body>

<section class="card card--contact">
  <div class="mark-large">
    <span class="mark-large__name">Stonefield</span>
  </div>
  <div class="contact">
    <h1 class="contact__name">Marcus Tilley</h1>
    <div class="contact__rule"></div>
    <ul class="contact__list">
      <li class="contact__item">
        <svg class="contact__icon" viewBox="0 0 24 24" aria-hidden="true"><path fill="#e8891c" d="M6.6 10.8a15 15 0 0 0 6.6 6.6l2.2-2.2a1 1 0 0 1 1-.25 11.4 11.4 0 0 0 3.6.57 1 1 0 0 1 1 1V20a1 1 0 0 1-1 1A17 17 0 0 1 3 4a1 1 0 0 1 1-1h3.5a1 1 0 0 1 1 1c0 1.25.2 2.45.57 3.57a1 1 0 0 1-.25 1z"/></svg>
        208 367 4120
      </li>
      <li class="contact__item">
        <svg class="contact__icon" viewBox="0 0 24 24" aria-hidden="true"><rect x="2" y="5" width="20" height="14" fill="#e8891c"/><path d="M2 5l10 8 10-8" fill="none" stroke="#232323" stroke-width="2"/></svg>
        MarcusTilleySCB@mailbox-example.com
      </li>
      <li class="contact__item">
        <svg class="contact__icon" viewBox="0 0 24 24" aria-hidden="true"><circle cx="12" cy="12" r="10" fill="#e8891c"/><path d="M2 12h20M12 2c3 3 3 17 0 20M12 2c-3 3-3 17 0 20" fill="none" stroke="#232323" stroke-width="1.6"/></svg>
        Stonefieldcustombuilders-example.com
      </li>
    </ul>
  </div>
</section>

<section class="card card--brand">
  <div class="mark-large">
    <span class="mark-large__name">Stonefield</span>
  </div>
  <div class="brand">
    <span class="brand__square"></span>
    <span class="brand__name">Stonefield<br>Custom Builders</span>
  </div>
</section>

</body>
</html>
```